Business car for dental practice

I have a new logo. Want it use for a new business card design. Hi end dental practice Would like a scan code on it for quick access to my web site and mobile site too. Green and purple are in logo design. Maybe have scan code on back? My website is peterhalvorsenDDS.example
Updates

Lakemont Crest Dental Associates

248 N Fairlawn Ave
Elmhaven, NY 10990
555-318-4072

317 N Wexford Rd. 
Suite 406
Mt. Harlow, NY 10991
555-762-1938

would like to incorporate logo, and addresses of both offices, and I recently saw a business card with a scan box on it which would bring people directly to the web site. if anyone knows how to do that, that could possibly go on the back of the card. (May be something I have to add at printing process) card can be one sided, or two sided.  

Reason: designer is revising for me. has not posted changes yet. hope he does soon!!

Industry/Entity Type

Business

```html
<!DOCTYPE html>
<html lang="en">
<head>
<meta charset="utf-8">
<title>Lakemont Crest Dental Associates – Business Cards</title>
<link rel="stylesheet" href="https://fonts.googleapis.com/css2?family=Gelasio:wght@400&family=Open+Sans:wght@700&family=Crimson+Text:wght@400&display=swap">
<style>
  :root {
    --page: #ffffff;
    --card: #ffffff;
    --plum-text: #8a2372;
    --ink-light: #ffffff;
    --shadow: rgba(60, 80, 110, 0.28);
  }
  html, body {
    margin: 0;
    padding: 0;
    width: 1140px;
    height: 1200px;
    overflow: hidden;
    background: var(--page);
  }
  .sheet {
    position: relative;
    width: 1140px;
    height: 1200px;
  }
  .card {
    position: absolute;
    left: 342px;
    width: 457px;
    height: 271px;
    background: var(--card);
    box-shadow: 0 6px 22px var(--shadow);
    overflow: hidden;
  }
  .card--front { top: 305px; }
  .card--back  { top: 666px; }
  .card__wave {
    position: absolute;
    inset: 0;
    width: 457px;
    height: 271px;
  }
  .brand {
    position: absolute;
    display: flex;
    align-items: center;
  }
  .brand__square {
    background: var(--plum-text);
    flex: none;
  }
  .card--front .brand {
    left: 60px;
    top: 52px;
    gap: 8px;
  }
  .card--front .brand__square {
    width: 58px;
    height: 58px;
  }
  .brand__name {
    margin: 0;
    font-family: "Gelasio", Georgia, serif;
    font-weight: 400;
    color: var(--plum-text);
    line-height: 1;
  }
  .brand__name-main {
    display: block;
    font-size: 37px;
    letter-spacing: -0.3px;
  }
  .brand__name-sub {
    display: block;
    font-size: 16px;
    letter-spacing: 4.4px;
    margin-top: 1px;
    text-align: center;
  }
  .office {
    position: absolute;
    top: 180px;
    margin: 0;
    font-family: "Open Sans", Arial, sans-serif;
    font-weight: 700;
    font-size: 12.5px;
    line-height: 17.5px;
    color: var(--ink-light);
    font-style: normal;
  }
  .office--west { left: 15px; text-align: left; }
  .office--east { right: 15px; text-align: right; }
  .card--back .brand__square {
    position: absolute;
    left: 194px;
    top: 36px;
    width: 79px;
    height: 79px;
  }
  .back-name {
    position: absolute;
    left: 0;
    right: 0;
    top: 196px;
    margin: 0;
    text-align: center;
    font-family: "Crimson Text", Georgia, serif;
    font-weight: 400;
    color: var(--ink-light);
    text-transform: uppercase;
    line-height: 1;
  }
  .back-name__main {
    display: block;
    font-size: 23px;
    letter-spacing: 0.3px;
  }
  .back-name__sub {
    display: block;
    font-size: 12.5px;
    letter-spacing: 0.4px;
    margin-top: 3px;
  }
</style>
</head>
<body>
<main class="sheet">

  <section class="card card--front" aria-label="Business card front">
    <svg class="card__wave" viewBox="0 0 457 271" aria-hidden="true">
      <defs>
        <linearGradient id="plum-fill-front" x1="0" y1="0" x2="0" y2="1">
          <stop offset="0" stop-color="#9c2a7e"/>
          <stop offset="1" stop-color="#5b2252"/>
        </linearGradient>
        <linearGradient id="leaf-fill-front" x1="0" y1="0" x2="1" y2="0">
          <stop offset="0" stop-color="#3e8a34"/>
          <stop offset="0.5" stop-color="#6cc046"/>
          <stop offset="1" stop-color="#3e8a34"/>
        </linearGradient>
      </defs>
      <path d="M0 133 Q228 178 457 133 L457 271 L0 271 Z" fill="url(#leaf-fill-front)"/>
      <path d="M0 149 Q228 186 457 149 L457 271 L0 271 Z" fill="url(#plum-fill-front)"/>
    </svg>

    <div class="brand">
      <span class="brand__square" aria-hidden="true"></span>
      <h1 class="brand__name">
        <span class="brand__name-main">Lakemont Crest</span>
        <span class="brand__name-sub">Dental Associates</span>
      </h1>
    </div>

    <address class="office office--west">
      Lakemont Crest Dental Associates<br>
      248 N Fairlawn Ave<br>
      Elmhaven, NY 10990<br>
      555-318-4072
    </address>
    <address class="office office--east">
      317 N Wexford Rd.<br>
      Suite 406<br>
      Mt. Harlow, NY 10991<br>
      555-762-1938
    </address>
  </section>

  <section class="card card--back" aria-label="Business card back">
    <svg class="card__wave" viewBox="0 0 457 271" aria-hidden="true">
      <defs>
        <linearGradient id="plum-fill-back" x1="0" y1="0" x2="0" y2="1">
          <stop offset="0" stop-color="#9c2a7e"/>
          <stop offset="1" stop-color="#5b2252"/>
        </linearGradient>
        <linearGradient id="leaf-fill-back" x1="0" y1="0" x2="1" y2="0">
          <stop offset="0" stop-color="#3e8a34"/>
          <stop offset="0.5" stop-color="#6cc046"/>
          <stop offset="1" stop-color="#3e8a34"/>
        </linearGradient>
      </defs>
      <path d="M0 133 Q228 178 457 133 L457 271 L0 271 Z" fill="url(#leaf-fill-back)"/>
      <path d="M0 149 Q228 186 457 149 L457 271 L0 271 Z" fill="url(#plum-fill-back)"/>
    </svg>

    <span class="brand__square" aria-hidden="true"></span>

    <h2 class="back-name">
      <span class="back-name__main">Lakemont Crest</span>
      <span class="back-name__sub">Dental Associates</span>
    </h2>
  </section>

</main>
</body>
</html>
```